Business Card Design Project

We are rebranding an existing automotive collision repair business. The business is called dentworks garage. I have attached logo but I'm not tied to that. I want to leave this wide open.

I want this card to say we are professional, competent, cutting edge. We are focused on customers and use a lot of the latest technology to make the customer experience different. We sign customers in on iPads. Paperwork I signed electronically and updates are sent via text, email, logging on a website or as they wish. I want this innovation and image to come through in our cards

Target Market(s)

60%. Women 40% men. Age 35-60

Industry/Entity Type

Automotive

Requirements
Must have
• The card must have name, title, phone,email, cell, web page

```html
<!DOCTYPE html>
<html lang="en">
<head>
<meta charset="utf-8">
<title>Dentworks Garage — Business Card</title>
<link href="https://fonts.googleapis.com/css2?family=PT+Sans+Narrow:wght@400;700&display=swap" rel="stylesheet">
<style>
  :root {
    --backdrop: #e0e0e0;
    --card-light: #ffffff;
    --card-dark: #1b1b1b;
    --brand-green: #6db02a;
    --ink: #1e1e1e;
  }
  * { margin: 0; padding: 0; box-sizing: border-box; }
  html, body {
    width: 1200px;
    height: 849px;
    overflow: hidden;
    background: var(--backdrop);
    font-family: "PT Sans Narrow", "Arial Narrow", sans-serif;
    color: var(--ink);
  }
  .canvas { position: relative; width: 1200px; height: 849px; }

  .card {
    position: absolute;
    top: 290px;
    width: 467px;
    height: 267px;
    border-radius: 13px;
    overflow: hidden;
  }
  .card--front { left: 98px; background: var(--card-light); }
  .card--back  { left: 634px; background: var(--card-dark); }

  .front-band {
    position: absolute;
    left: 0; right: 0; bottom: 0;
    height: 24px;
    background: var(--brand-green);
  }

  .brand-name {
    position: absolute;
    white-space: nowrap;
    font-weight: 700;
    color: var(--brand-green);
    transform: translate(-50%, -50%);
    letter-spacing: 0.2px;
  }
  .card--front .brand-name { left: 125px; top: 112px; font-size: 27px; }
  .card--back  .brand-name { left: 233px; top: 138px; font-size: 50px; }

  .person { position: absolute; left: 253px; top: 12px; }
  .person-name {
    font-size: 25px;
    color: var(--brand-green);
    line-height: 1.1;
  }
  .person-title { font-size: 11px; line-height: 1.2; }

  .contact-list {
    position: absolute;
    left: 259px;
    top: 133px;
    list-style: none;
  }
  .contact-item {
    display: flex;
    align-items: center;
    height: 16.5px;
    font-size: 11px;
  }
  .contact-icon { width: 10px; height: 10px; margin-right: 8px; flex: none; }
</style>
</head>
<body>
<div class="canvas">

  <section class="card card--front">
    <div class="brand-name">Dentworks Garage</div>

    <div class="person">
      <div class="person-name">Your Name</div>
      <div class="person-title">Tittle</div>
    </div>

    <ul class="contact-list">
      <li class="contact-item">
        <svg class="contact-icon" viewBox="0 0 10 10"><rect x="0.5" y="2" width="9" height="6.5" fill="#1e1e1e"/><path d="M0.5 2 L5 5.8 L9.5 2" stroke="#fff" stroke-width="0.9" fill="none"/></svg>
        1111 Address, xxxxxxxx xxxxxxxx -xx
      </li>
      <li class="contact-item">
        <svg class="contact-icon" viewBox="0 0 10 10"><path d="M2 1 L3.8 1 L4.4 3.4 L3.2 4.3 C3.8 5.6 4.6 6.4 5.8 7 L6.7 5.8 L9 6.4 L9 8.2 C9 8.8 8.5 9.2 7.8 9.1 C4.2 8.6 1.5 5.8 1 2.2 C0.9 1.5 1.3 1 2 1 Z" fill="#1e1e1e"/></svg>
        000 000 000
      </li>
      <li class="contact-item">
        <svg class="contact-icon" viewBox="0 0 10 10"><rect x="0.5" y="1.5" width="9" height="7" rx="1" fill="#1e1e1e"/><circle cx="5" cy="5" r="2" fill="#fff"/><circle cx="5" cy="5" r="1" fill="#1e1e1e"/></svg>
        e-mail : xxxx_xxx@dentworksmail.com
      </li>
      <li class="contact-item">
        <svg class="contact-icon" viewBox="0 0 10 10"><rect x="1.5" y="2" width="5" height="7.5" rx="0.8" fill="#1e1e1e"/><rect x="2.4" y="3" width="3.2" height="3" fill="#fff"/><path d="M7 2.5 A2 2 0 0 1 8.5 1 M7.3 3.5 A3 3 0 0 1 9.5 0.8" stroke="#1e1e1e" stroke-width="0.7" fill="none"/></svg>
        000 000 000
      </li>
      <li class="contact-item">
        <svg class="contact-icon" viewBox="0 0 10 10"><circle cx="5" cy="5" r="4.4" fill="#1e1e1e"/><path d="M0.6 5 H9.4 M5 0.6 C3 3 3 7 5 9.4 M5 0.6 C7 3 7 7 5 9.4" stroke="#fff" stroke-width="0.7" fill="none"/></svg>
        Website : xxxxxxxx xxxx xxx xxxx xxx
      </li>
    </ul>

    <div class="front-band"></div>
  </section>

  <section class="card card--back">
    <div class="brand-name">Dentworks Garage</div>
  </section>

</div>
</body>
</html>
```